Criação de Kit Layout de Posts para Redes Sociais (Facebook, Instagram e etc) para Construção & Engenharia
A empresa queria:
" TRABALHAMOS COM LOCAÇÃO, VENDA DE EQUIPAMENTOS, MONTAGEM E PROJETOS DE ANDAIME E ESCORAMENTO "

```html
<!DOCTYPE html>
<html lang="pt-BR">
<head>
<meta charset="UTF-8">
<title>Torva Equipamentos – Não deixe sua obra parar</title>
<link href="https://fonts.googleapis.com/css2?family=Montserrat:wght@400;500;700;800;900&display=swap" rel="stylesheet">
<style>
  :root {
    --bg-dark: #2b2b2b;
    --bg-mid: #4a4a4a;
    --bg-light: #6b6b6b;
    --yellow: #f3c12f;
    --yellow-deep: #e9b21f;
    --ink: #2e2e2e;
    --white: #ffffff;
    --glow: rgba(255, 214, 90, 0.55);
  }
  * { margin: 0; padding: 0; box-sizing: border-box; }
  html, body { width: 1200px; height: 1200px; overflow: hidden; }
  body { font-family: "Montserrat", sans-serif; background: var(--bg-dark); }

  .post {
    position: relative;
    width: 1200px;
    height: 1200px;
    overflow: hidden;
  }

  .site-photo {
    position: absolute;
    inset: 0;
    background:
      linear-gradient(90deg, rgba(0,0,0,0.35) 0%, rgba(0,0,0,0) 40%, rgba(0,0,0,0.25) 100%),
      linear-gradient(180deg, var(--bg-light) 0%, var(--bg-mid) 45%, var(--bg-dark) 100%);
  }

  .glow {
    position: absolute;
    left: 820px;
    top: 640px;
    width: 480px;
    height: 480px;
    border-radius: 50%;
    background: radial-gradient(circle, var(--glow) 0%, rgba(255,214,90,0.15) 35%, rgba(255,214,90,0) 70%);
  }

  .social-handle {
    position: absolute;
    top: 28px;
    right: 26px;
    display: flex;
    align-items: center;
    gap: 12px;
    color: var(--white);
    font-weight: 500;
    font-size: 22px;
    letter-spacing: 3px;
  }
  .social-handle .dot {
    width: 24px;
    height: 24px;
    border-radius: 50%;
    background: var(--yellow);
  }

  .message-card {
    position: absolute;
    left: 156px;
    top: 262px;
    width: 900px;
    height: 632px;
    border-radius: 48px;
    background: linear-gradient(160deg, var(--yellow) 0%, var(--yellow-deep) 100%);
    color: var(--ink);
  }

  .headline {
    position: absolute;
    top: 86px;
    left: 0;
    right: 0;
    text-align: center;
    font-weight: 800;
    font-size: 62px;
    line-height: 72px;
    letter-spacing: 1px;
  }
  .headline .pill {
    display: inline-block;
    background: var(--ink);
    color: var(--yellow);
    border-radius: 40px;
    padding: 0 20px;
    line-height: 64px;
  }

  .subline {
    position: absolute;
    top: 266px;
    left: 0;
    right: 0;
    text-align: center;
    font-weight: 400;
    font-size: 44px;
    line-height: 62px;
  }
  .subline strong { font-weight: 800; }

  .brand {
    position: absolute;
    left: 72px;
    top: 452px;
  }
  .brand-name {
    display: flex;
    align-items: center;
    gap: 16px;
    color: var(--white);
    font-weight: 800;
    font-size: 64px;
    line-height: 64px;
    letter-spacing: 2px;
  }
  .brand-name .mark {
    width: 52px;
    height: 52px;
    background: var(--white);
  }
  .brand-tag {
    margin-left: 68px;
    margin-top: 6px;
    color: var(--white);
    font-weight: 500;
    font-size: 19px;
    letter-spacing: 7px;
  }
  .brand-partners {
    margin-top: 12px;
    color: var(--ink);
    font-weight: 700;
    font-size: 16px;
    letter-spacing: 1px;
  }
</style>
</head>
<body>
  <main class="post">
    <div class="site-photo" role="img" aria-label="Fachada de edifício em construção com andaimes, em tons de cinza"></div>
    <div class="glow"></div>

    <div class="social-handle">
      <span class="dot"></span>
      <span>@TORVAEQUIPAMENTOS</span>
    </div>

    <section class="message-card">
      <h1 class="headline">NÃO DEIXE SUA<br>OBRA <span class="pill">PARAR.</span></h1>
      <p class="subline">Conte com nossos equipamentos<br>para <strong>AGILIZAR</strong> sua obra.</p>

      <div class="brand">
        <div class="brand-name"><span class="mark"></span>TORVA</div>
        <div class="brand-tag">EQUIPAMENTOS</div>
        <div class="brand-partners">VERTIX ANDAIMES | BRAVIMAQ</div>
      </div>
    </section>
  </main>
</body>
</html>
```